CREATE A BUSINESS CARD FOR A BOAT CLEANING SERVICE

WE ARE STARTING A NEW BOAT CLEANING BUSINESS. WE DIVE UNDERWATER TO CLEAN BOAT HULLS, JETTIES, UNDERWATER STRUCTURES ETC. WE ARE LOOKING FOR AN UPPERMARKET MODERN LOGO AND BUSINESS CARD AS ALOT OF OUR TARGET MARKET WILL BE HIGH END. YOU HAVE TO DESIGN A BUSINESS CARD AND LOGO SEPERATELY .
THE BUSINESS CARD DIMESNION MUST BE STANDARD SIZE.
The standard dimensions of a printed business card are 3.5 x 2 inches

Target Market(s)

UNDERWATER SERVICED

Industry/Entity Type

Business

Contact Information for Business Card

HALDEN UNDERWATER SERVICES

Font styles to use
Serif

Colors

Designer to choose colors to be used in the design.

Requirements
Must have
• HALDEN
Nice to have
• dark
Should not have
• more than 3 colors

```html
<!DOCTYPE html>
<html lang="en">
<head>
<meta charset="utf-8">
<title>Halden Underwater Services – Business Card</title>
<link href="https://fonts.googleapis.com/css2?family=Montserrat:wght@300;400;500;600&display=swap" rel="stylesheet">
<style>
  :root {
    --page-bg: #e9eaec;
    --card-white: #ffffff;
    --ink-blue: #1a78b8;
    --deep-blue: #0d5a99;
    --light-blue: #3d9bd2;
    --ink-grey: #9a9ea3;
    --band-grey: #b7babd;
  }
  * { margin: 0; padding: 0; box-sizing: border-box; }
  html, body { width: 1200px; height: 1023px; overflow: hidden; }
  body {
    background: var(--page-bg);
    font-family: "Montserrat", sans-serif;
    position: relative;
  }
  .card {
    position: absolute;
    top: 196px;
    width: 360px;
    height: 630px;
    background: var(--card-white);
    border-radius: 18px;
    overflow: hidden;
    box-shadow: 0 10px 30px rgba(0,0,0,0.18);
  }
  .card--front { left: 180px; }
  .card--back { left: 660px; }

  .brand { position: absolute; left: 0; right: 0; top: 92px; text-align: center; }
  .brand__name {
    color: var(--ink-blue);
    font-size: 34px;
    font-weight: 400;
    letter-spacing: 14px;
    padding-left: 14px;
  }
  .brand__tag {
    color: var(--ink-grey);
    font-size: 12.5px;
    font-weight: 300;
    letter-spacing: 5px;
    padding-left: 5px;
    margin-top: 4px;
  }

  .contact { position: absolute; left: 40px; top: 230px; }
  .contact__name { color: var(--ink-blue); font-size: 26px; font-weight: 500; letter-spacing: 1px; }
  .contact__role { color: var(--ink-grey); font-size: 13px; font-weight: 300; margin-top: 2px; }
  .contact__rule { width: 22px; height: 2px; background: var(--ink-blue); margin: 12px 0 14px; }
  .contact__line { color: var(--ink-grey); font-size: 13px; font-weight: 300; line-height: 19px; display: flex; align-items: center; }
  .contact__line svg { width: 11px; height: 11px; margin-right: 7px; fill: var(--ink-grey); }
  .contact__line--web { color: var(--ink-blue); }
  .contact__spacer { height: 8px; }

  .band { position: absolute; left: 0; bottom: 0; width: 360px; height: 210px; }
  .band-logo {
    position: absolute;
    bottom: 34px;
    display: flex;
    align-items: center;
    color: #ffffff;
    font-size: 18px;
    font-weight: 600;
    letter-spacing: 2px;
  }
  .band-logo__dot { width: 16px; height: 16px; border-radius: 50%; background: #ffffff; margin-right: 8px; opacity: .85; }
  .card--front .band-logo { left: 120px; }
  .card--back .band-logo { left: 120px; }
  .badge { position: absolute; left: 28px; bottom: 30px; width: 46px; height: 30px; border-radius: 50%; background: rgba(255,255,255,0.25); }
</style>
</head>
<body>

  <section class="card card--front">
    <div class="brand">
      <div class="brand__name">HALDEN</div>
      <div class="brand__tag">UNDERWATER SERVICE</div>
    </div>

    <div class="contact">
      <div class="contact__name">DANIEL REEVE</div>
      <div class="contact__role">President</div>
      <div class="contact__rule"></div>
      <div class="contact__line">140, 318- 9th Ave. SW</div>
      <div class="contact__line">Calgary, AB T2P 1K4</div>
      <div class="contact__spacer"></div>
      <div class="contact__line"><svg viewBox="0 0 12 12"><path d="M2.5 1 L4.5 1 L5.2 3.5 L4 4.6 C4.8 6.2 5.8 7.2 7.4 8 L8.5 6.8 L11 7.5 L11 9.5 C11 10.3 10.3 11 9.5 11 C5 11 1 7 1 2.5 C1 1.7 1.7 1 2.5 1Z"/></svg>(410) 555-0182</div>
      <div class="contact__line"><svg viewBox="0 0 12 12"><path d="M1 2.5 H11 V9.5 H1 Z M1.8 3.2 L6 6.3 L10.2 3.2" fill="none" stroke="#9a9ea3" stroke-width="1.2"/></svg>info@haldenunderwater.com</div>
      <div class="contact__line contact__line--web"><svg viewBox="0 0 12 12"><circle cx="6" cy="6" r="4.8" fill="none" stroke="#9a9ea3" stroke-width="1.1"/><path d="M1.2 6 H10.8 M6 1.2 C3.5 4 3.5 8 6 10.8 M6 1.2 C8.5 4 8.5 8 6 10.8" fill="none" stroke="#9a9ea3" stroke-width="0.9"/></svg>www.haldenunderwater.com</div>
    </div>

    <svg class="band" viewBox="0 0 360 210" aria-hidden="true">
      <defs>
        <linearGradient id="blueFront" x1="0" y1="0" x2="1" y2="1">
          <stop offset="0" stop-color="#3d9bd2"/>
          <stop offset="1" stop-color="#0d5a99"/>
        </linearGradient>
      </defs>
      <path d="M0 20 L360 80 L360 210 L0 210 Z" fill="url(#blueFront)"/>
      <path d="M0 20 L360 80 L360 110 L300 110 L240 165 L262 112 L0 70 Z" fill="#b7babd" stroke="#ffffff" stroke-width="3"/>
    </svg>
    <div class="badge"></div>
    <div class="band-logo"><span class="band-logo__dot"></span>HALDEN</div>
  </section>

  <section class="card card--back">
    <div class="brand" style="top:120px">
      <div class="brand__name">HALDEN</div>
      <div class="brand__tag">UNDERWATER SERVICE</div>
    </div>

    <svg class="band" viewBox="0 0 360 210" style="height:330px" preserveAspectRatio="none" aria-hidden="true">
      <defs>
        <linearGradient id="blueBack" x1="0" y1="0" x2="1" y2="1">
          <stop offset="0" stop-color="#1a78b8"/>
          <stop offset="1" stop-color="#0d5a99"/>
        </linearGradient>
      </defs>
      <path d="M0 30 L360 0 L360 210 L0 210 Z" fill="url(#blueBack)"/>
      <path d="M0 30 L360 0 L360 20 L300 90 L290 40 L0 60 Z" fill="#b7babd" stroke="#ffffff" stroke-width="3"/>
    </svg>
    <div class="badge"></div>
    <div class="band-logo"><span class="band-logo__dot"></span>HALDEN</div>
  </section>

</body>
</html>
```